Social Media Marketing website

Need website designed for social media marketing company BrightLoop.com
Do no currently have logo.
Pages:
Main
Services
Order
Contact
Please use dummy text for now. I will provide content to winner later to add.
Main page should clearly show the steps with some sort of graphic: Establish, Engage, Analyze.
Services provided (steps):
1) Establish social media presence
2) Social media management and advertising
3) Analyze and engage
Site should be simple, clean and attractive. Design examples:
http://plinkster.com/
http://www.quillbase.com/
http://www.harrowvalemq.com/
Be creative! It should not look like a template.
Updates
Updated examples.
Contact me for questions.
dave@brightloop.com
3) Analyze and engage
Advertising

```html
<!DOCTYPE html>
<html lang="en">
<head>
<meta charset="utf-8">
<title>BrightLoop.com</title>
<link rel="stylesheet" href="https://fonts.googleapis.com/css2?family=Roboto:wght@300;400;500&family=Josefin+Sans:wght@300;400&family=Michroma&display=swap">
<style>
  :root {
    --brand-blue: #1b8ad8;
    --ink: #222833;
    --nav-top: #a9c6f7;
    --nav-bottom: #5d8ee9;
    --nav-line: #ffffff;
    --step-blue: #2f5fd2;
    --panel-blue: #6b99ef;
    --button-line: #c3c8d2;
    --button-text: #5d6b86;
    --stage-black: #000000;
    --stage-grey: #6a6a6a;
    --photo-frame: #b98c3c;
    --photo-warm: #b97a52;
    --photo-deep: #6e4128;
    --gold-text: #f2c94c;
    --alert-red: #e01010;
    --login-grey: #bfbfbf;
    --field-white: #f4f4f4;
    --ad-fill: #c6c7e3;
    --ad-line: #ffffff;
    --social-yellow: #f4c04e;
    --social-panel: #d4d4d4;
    --white: #ffffff;
  }
  * { box-sizing: border-box; margin: 0; padding: 0; }
  html, body { width: 1200px; height: 975px; overflow: hidden; background: var(--white); }
  body { position: relative; font-family: "Roboto", Arial, sans-serif; color: var(--ink); }
  .abs { position: absolute; }

  .brand { left: 15px; top: 30px; font: 300 46px "Roboto", sans-serif; color: var(--brand-blue); letter-spacing: 0.5px; }
  .account-links { top: 64px; font: 300 27px "Roboto", sans-serif; color: var(--ink); }
  .account-links.login { left: 990px; }
  .account-links.signup { left: 1089px; }

  .main-nav { left: 10px; top: 105px; width: 1175px; height: 76px;
    background: linear-gradient(var(--nav-top), var(--nav-bottom)); }
  .nav-item { position: absolute; top: 0; height: 76px; text-align: center;
    font: 300 28px "Roboto", sans-serif; line-height: 76px; color: var(--ink); border-right: 2px solid var(--nav-line); }
  .nav-item.current { color: var(--white); }
  .search-label { position: absolute; left: 765px; top: 0; font: 300 27px "Roboto", sans-serif; line-height: 76px; }
  .search-field { position: absolute; left: 870px; top: 21px; width: 268px; height: 35px; border-radius: 6px;
    background: linear-gradient(#e8e8e8, #ffffff); }
  .search-field svg { position: absolute; right: 6px; top: 5px; }

  .sidebar { left: 10px; top: 183px; width: 377px; height: 765px;
    background: linear-gradient(var(--white) 0%, var(--white) 16.5%, var(--panel-blue) 16.5%, var(--panel-blue) 24%, var(--white) 24%, var(--white) 85%, var(--panel-blue) 100%); }
  .tab-button { position: absolute; width: 178px; height: 31px; border: 2px solid var(--button-line); border-radius: 6px;
    background: var(--white); text-align: center; font: 300 18px "Roboto", sans-serif; line-height: 27px; color: var(--button-text); }
  .steps-title { position: absolute; left: 8px; top: 137px; white-space: nowrap;
    font: 300 27px "Roboto", sans-serif; line-height: 36px; color: var(--white); }
  .step-card { position: absolute; left: 5px; width: 368px; height: 105px; background: var(--white);
    border: 2px solid var(--panel-blue); text-align: center; font: 300 23px "Roboto", sans-serif; line-height: 30px; color: var(--step-blue); padding: 14px 8px 0; }
  .step-card .step-mark { position: absolute; right: 10px; bottom: 8px; width: 40px; height: 40px; border-radius: 50%;
    background: radial-gradient(#eeeeee, #c9c9c9); z-index: 0; }
  .step-card span { position: relative; z-index: 1; }
  .social-panel { position: absolute; left: -2px; top: 522px; width: 375px; height: 128px; border-radius: 10px;
    background: linear-gradient(#f0f0f0, var(--social-panel)); }
  .social-button { position: absolute; left: 25px; width: 274px; height: 34px; background: var(--social-yellow);
    border-radius: 4px; font: 300 21px "Roboto", sans-serif; line-height: 34px; text-align: center; }
  .social-square { position: absolute; left: 304px; width: 36px; height: 36px; background: var(--nav-bottom); border-radius: 4px; }
  .free-note { position: absolute; left: 0; top: 684px; width: 377px; text-align: center; font: 300 20px "Roboto", sans-serif; line-height: 27px; }

  .stage { left: 393px; top: 183px; width: 792px; height: 765px;
    background: linear-gradient(180deg, var(--stage-black) 0%, var(--stage-black) 55%, var(--stage-grey) 100%); }
  .feature-photo { position: absolute; left: 32px; top: 14px; width: 354px; height: 220px; border: 5px solid var(--photo-frame);
    background: radial-gradient(circle at 50% 55%, var(--photo-warm), var(--photo-deep)); }
  .headline { position: absolute; left: 0; top: 247px; width: 428px; text-align: center;
    font: 300 36px "Josefin Sans", sans-serif; line-height: 43px; color: var(--white); letter-spacing: 1px; }
  .tip { position: absolute; left: 87px; font: 17px "Michroma", sans-serif; line-height: 20px; color: var(--gold-text); width: 290px; }
  .tip-icon { position: absolute; left: 57px; }
  .learn { position: absolute; left: 87px; font: 11px "Michroma", sans-serif; color: var(--white); }

  .login-title { position: absolute; left: 472px; top: 113px; font: 19px "Michroma", sans-serif; color: var(--alert-red); }
  .login-box { position: absolute; left: 459px; top: 147px; width: 340px; height: 135px; border-radius: 12px 0 0 12px;
    background: linear-gradient(90deg, #9a9a9a, var(--login-grey) 10%, #d8d8d8); }
  .field-label { position: absolute; left: 60px; font: 19px "Michroma", sans-serif; color: var(--ink); }
  .field { position: absolute; left: 58px; width: 233px; height: 25px; border-radius: 5px; background: var(--field-white); }
  .forgot { position: absolute; left: 467px; top: 290px; font: 17px "Michroma", sans-serif; color: var(--alert-red); }
  .signup-button { position: absolute; left: 570px; top: 330px; width: 113px; height: 42px; border-radius: 8px;
    background: linear-gradient(#4a6a9a, #12233f); border: 2px solid #8fa6c8; color: var(--white);
    font: 500 20px "Roboto", sans-serif; line-height: 38px; text-align: center; }

  .ad-slot { position: absolute; background: var(--ad-fill); border: 2px solid var(--ad-line);
    display: flex; align-items: center; justify-content: center; font: 300 24px "Roboto", sans-serif; color: var(--ink); }

  .copyright { left: 0; top: 953px; width: 1215px; text-align: center; font: 11px "Roboto", sans-serif; }
</style>
</head>
<body>
  <div class="abs brand">BrightLoop.com</div>
  <div class="abs account-links login">Login</div>
  <div class="abs account-links signup">Sign up</div>

  <nav class="abs main-nav">
    <div class="nav-item current" style="left:0;width:156px;">MAIN</div>
    <div class="nav-item" style="left:156px;width:154px;">SERVICE</div>
    <div class="nav-item" style="left:310px;width:152px;">ORDER</div>
    <div class="nav-item" style="left:462px;width:150px;">CONTACT</div>
    <div class="search-label">Search</div>
    <div class="search-field">
      <svg width="26" height="26" viewBox="0 0 26 26"><circle cx="10" cy="10" r="7" fill="none" stroke="#777" stroke-width="2"/><line x1="15" y1="15" x2="23" y2="23" stroke="#777" stroke-width="3"/></svg>
    </div>
  </nav>

  <aside class="abs sidebar">
    <div class="tab-button" style="left:5px;top:17px;">HOW IT WORKS ?</div>
    <div class="tab-button" style="left:191px;top:17px;">GET CONTENT</div>
    <div class="tab-button" style="left:5px;top:54px;">MEMBERS</div>
    <div class="tab-button" style="left:191px;top:54px;">CLIENT</div>
    <div class="tab-button" style="left:5px;top:91px;">PRODUCT</div>
    <div class="tab-button" style="left:191px;top:91px;">SUPPORT</div>
    <div class="steps-title">SERVICE PROVIDED (STEPS)</div>
    <div class="step-card" style="top:182px;"><div class="step-mark" role="img" aria-label="Speech bubble graphic"></div><span>Establish social media presence</span></div>
    <div class="step-card" style="top:291px;padding-top:6px;"><div class="step-mark" role="img" aria-label="Coin graphic"></div><span>Social media management and Advertising</span></div>
    <div class="step-card" style="top:399px;"><div class="step-mark" role="img" aria-label="Pencil graphic"></div><span>Analyze and engage</span></div>
    <div class="social-panel">
      <div class="social-button" style="top:20px;">Sign in with Friendwall</div>
      <div class="social-square" style="top:19px;"></div>
      <div class="social-button" style="top:68px;">Sign in with Chirpline</div>
      <div class="social-square" style="top:67px;"></div>
    </div>
    <div class="free-note">Its totally free to be registered with us<br>and easy to use</div>
  </aside>

  <main class="abs stage">
    <div class="feature-photo" role="img" aria-label="Photo of clay figures standing in a circle holding hands"></div>
    <h1 class="headline">JOIN WITH US AND<br>BUILD YOUR<br>NETWORK</h1>

    <svg class="tip-icon" style="top:378px;" width="26" height="26" viewBox="0 0 26 26"><path d="M4 22 L7 15 L19 3 L23 7 L11 19 Z" fill="#e0b030" stroke="#6a4a10"/></svg>
    <div class="tip" style="top:393px;">Business success tips</div>
    <div class="learn" style="top:419px;">Learn more....</div>
    <svg class="tip-icon" style="top:430px;" width="26" height="26" viewBox="0 0 26 26"><path d="M4 22 L7 15 L19 3 L23 7 L11 19 Z" fill="#e0b030" stroke="#6a4a10"/></svg>
    <div class="tip" style="top:445px;">social network for business</div>
    <div class="learn" style="top:492px;">Learn more....</div>
    <svg class="tip-icon" style="top:505px;" width="26" height="26" viewBox="0 0 26 26"><path d="M4 22 L7 15 L19 3 L23 7 L11 19 Z" fill="#e0b030" stroke="#6a4a10"/></svg>
    <div class="tip" style="top:518px;">how to build network</div>
    <div class="learn" style="top:540px;">Learn more....</div>

    <div class="login-title">Log in</div>
    <div class="login-box">
      <div class="field-label" style="top:10px;">User</div>
      <div class="field" style="top:35px;"></div>
      <div class="field-label" style="top:68px;">Password</div>
      <div class="field" style="top:93px;"></div>
    </div>
    <div class="forgot">Forgot your password?</div>
    <div class="signup-button">Sign Up</div>

    <div class="ad-slot" style="left:462px;top:414px;width:323px;height:109px;">ADVERTISEMENT</div>
    <div class="ad-slot" style="left:462px;top:529px;width:323px;height:110px;">ADVERTISEMENT</div>
    <div class="ad-slot" style="left:462px;top:644px;width:323px;height:112px;">ADVERTISEMENT</div>
    <div class="ad-slot" style="left:43px;top:644px;width:350px;height:112px;">ADVERTISEMENT</div>
  </main>

  <footer class="abs copyright">Copyright 2011 - BrightLoop.com- All Right Reserved</footer>
</body>
</html>
```